Website Redesign Brief for Breezeline Cooling Services WA

Creating a clear and concise brief for designers to redesign your website, https://breezelinecowa.com.au/, is essential to ensure the project aligns with your vision for a more energetic, friendly, optimistic, and user-friendly website. Below is a sample brief tailored to your request, balancing specificity with flexibility to allow designers to bring their creativity to the table.

Website Redesign Brief for Westwind Air Co
1. Project Overview

We are seeking a redesign of our website, https://breezelinecowa.com.au/, to create a vibrant, engaging, and user-friendly online presence that reflects our brand’s commitment to providing top-notch air conditioning services in Western Australia. The redesigned website should feel energetic, friendly, and optimistic while maintaining professionalism and improving user experience.
2. Goals and Objectives

Enhance Brand Perception: Convey a modern, approachable, and positive brand identity that resonates with both residential and commercial clients.
Improve User Experience: Simplify navigation, improve accessibility, and ensure a seamless experience across devices (desktop, tablet, mobile).
Increase Engagement: Encourage visitors to explore services, request quotes, and contact us through clear calls-to-action (CTAs).
Boost Conversion Rates: Make it easier for users to find information and take action (e.g., booking services or inquiries).
Showcase Expertise: Highlight our professional air conditioning services, experience, and customer satisfaction in an inviting way.

3. Target Audience

Primary Audience: Homeowners and small business owners in Western Australia seeking air conditioning installation, maintenance, or repair services.
Secondary Audience: Property managers, commercial clients, and real estate professionals looking for reliable HVAC solutions.
Demographics: Ages 25–65, mix of tech-savvy and non-tech-savvy users, located primarily in Perth and surrounding areas.
User Needs: Clear information about services, transparent pricing, easy contact options, and reassurance of quality and reliability.

4. Design Preferences

Tone and Style:

Energetic: Use bold, vibrant colors (e.g., blues, whites, and pops of warm tones like orange or yellow) to evoke energy and optimism.
Friendly: Incorporate approachable language, welcoming imagery, and a clean, uncluttered layout.
Optimistic: Highlight positive customer outcomes (e.g., comfort, energy savings) through visuals and messaging.
Professional yet approachable: Maintain credibility as a trusted service provider while avoiding a cold or overly corporate feel.

Visual Elements:

Use high-quality images of happy customers, comfortable homes/offices, and modern air conditioning units.
Incorporate subtle animations or micro-interactions to add energy (e.g., hover effects on buttons or smooth scrolling).
Avoid overly complex graphics that may slow down the site or distract from usability.

Typography: Clean, modern fonts that are easy to read. Use larger, bold headings for hierarchy and warmth.
Inspiration: Websites like https://www.frostvale.com.au/ (clean and professional) or https://www.quellarpowertech.com.au/ (user-friendly and modern) but with a more vibrant and welcoming vibe.

5. Functional Requirements

User-Friendly Navigation: Simplify the menu structure to make key pages (e.g., Services, About Us, Contact) easily accessible.
Mobile Responsiveness: Ensure the site is fully optimized for mobile devices, with fast load times and intuitive touch interactions.
Key Features:

Prominent CTAs for requesting quotes, booking services, or contacting the team.
A clear service overview with icons or visuals for each service (e.g., installation, repairs, maintenance).
A testimonials section to showcase customer satisfaction.
An easy-to-use contact form with minimal fields.
Integration with Google Maps for location-based services or office directions.

SEO and Performance: Optimize for search engines (e.g., keywords like “air conditioning Perth”) and ensure fast loading speeds.
Accessibility: Follow WCAG guidelines to ensure the site is usable for all visitors, including those with disabilities.

6. Content Guidance

Existing Content: Review and refine current content from https://breezelinecowa.com.au/ to make it concise, engaging, and aligned with the friendly tone.
New Content Ideas:

Add a “Why Choose Us” section highlighting expertise, customer service, and eco-friendly solutions.
Include a FAQ page to address common customer questions.
Create a blog section for tips on air conditioning maintenance or energy efficiency (optional).

Tone of Voice: Conversational, reassuring, and positive. Avoid technical jargon unless clearly explained.

7. Technical Considerations

Platform: Open to recommendations (e.g., WordPress, Wix, or custom-built) but prioritize ease of maintenance and scalability.
Integrations: Ensure compatibility with existing tools (e.g., Google Analytics, CRM for quote requests, or booking systems).
Domain and Hosting: Retain current domain (breezelinecowa.com.au); hosting recommendations welcome.
Timeline: Initial design concepts within [insert timeline, e.g., 2–3 weeks], with full redesign completed by [insert deadline, e.g., 6–8 weeks].
Budget: [Insert budget range or state “flexible, please provide a quote”].

8. Deliverables

Wireframes and mockups for homepage, service pages, and contact page.
Fully responsive website design with all necessary pages.
Style guide (colors, fonts, imagery guidelines).
CMS setup (if applicable) with basic training for content updates.
Testing and optimization for performance and SEO.

9. Success Metrics

Increased time on site and reduced bounce rate.
Higher conversion rates for quote requests and contact form submissions.
Positive user feedback on ease of navigation and overall experience.
Improved search engine rankings for key terms within [insert timeframe, e.g., 3 months].

10. Additional Notes

Please provide a portfolio of similar projects or examples of user-friendly, vibrant websites.
We are open to creative suggestions to make the website stand out in the HVAC industry.
Regular progress updates and collaboration during the design process are appreciated.
Updates

designers are asking for more time

few have requested an extension. I Have extended

Target Market(s)

Primary Audience: Homeowners and small business owners in Western Australia seeking air conditioning installation, maintenance, or repair services. Secondary Audience: Property managers, commercial clients, and real estate professionals looking for reliable HVAC solutions. Demographics: Ages 25–65, mix of tech-savvy and non-tech-savvy users, located primarily in Perth and surrounding areas. User Needs: Clear information about services, transparent pricing, easy contact options, and reassurance of quality and reliability.

Industry/Entity Type

Air Conditioning and Refrigeration (HVAC & R)

Coding

Coded - Design and coding required

Colors
0054AA
0677BA
7BADD7
CADEEF
E8F1F8
59FF00
82FF00
B8FF75
E3FFCB
F4FFEA
F0912C
F2A743
F7CA91
FBE8D2
FDF5EE
EE7325
F08F49
F5BC92
FAE3D3
FDF4ED

Requirements
Must have
• Must have all my current information I currently have on my web page.
Nice to have
• A sales page for people to buy products online

```html
<!DOCTYPE html>
<html lang="en">
<head>
<meta charset="utf-8">
<title>Westwind Air Co — Air Conditioning Repairs, Service and Installations</title>
<link rel="stylesheet" href="https://fonts.googleapis.com/css2?family=DM+Sans:wght@400;500;600;700&display=swap">
<style>
  :root {
    --ink: #111111;
    --ink-soft: #2b2b2b;
    --line: #ececec;
    --white: #ffffff;
    --peach: #FDF5EE;
    --orange: #EE7325;
    --navy: #0054AA;
    --photo-light: #e4e4e2;
    --photo-mid: #d2d3d1;
  }
  * { box-sizing: border-box; margin: 0; padding: 0; }
  html, body {
    width: 1200px; height: 1200px; overflow: hidden;
    font-family: "DM Sans", Arial, sans-serif;
    color: var(--ink);
    background: var(--white);
  }
  .page {
    width: 1200px; height: 1200px; position: relative; overflow: hidden;
    background: linear-gradient(165deg, var(--white) 0%, var(--peach) 45%, var(--white) 85%);
  }
  .site-header {
    height: 84px; display: flex; align-items: center;
    padding: 0 60px; border-bottom: 1px solid var(--line);
    background: var(--white);
  }
  .brand { display: flex; align-items: center; gap: 8px; font-weight: 700; font-size: 14px; color: var(--navy); white-space: nowrap; }
  .brand-dot { width: 30px; height: 30px; border-radius: 50%; background: var(--navy); flex: none; }
  .main-nav { margin-left: auto; display: flex; gap: 28px; align-items: center; }
  .main-nav a { font-size: 15px; font-weight: 500; color: var(--ink-soft); text-decoration: none; white-space: nowrap; }
  .btn {
    display: inline-flex; align-items: center; gap: 8px;
    background: var(--orange); color: var(--white);
    font-size: 15px; font-weight: 500; text-decoration: none;
    padding: 13px 22px; white-space: nowrap;
  }
  .site-header .btn { margin-left: 32px; }
  .btn svg { width: 14px; height: 14px; }
  .hero { text-align: center; padding-top: 84px; }
  .eyebrow { font-size: 15px; letter-spacing: 0.28em; text-transform: uppercase; font-weight: 500; color: var(--ink-soft); }
  .hero h1 { margin: 26px auto 0; font-size: 54px; line-height: 1.18; font-weight: 700; letter-spacing: -0.01em; max-width: 900px; }
  .hero p { margin: 30px auto 0; max-width: 760px; font-size: 16px; line-height: 1.75; color: var(--ink-soft); }
  .hero .btn { margin-top: 40px; }
  .about { position: absolute; left: 0; top: 640px; width: 1200px; height: 560px; }
  .about-text { position: absolute; left: 90px; top: 170px; width: 440px; }
  .about-text h2 { margin-top: 10px; font-size: 40px; font-weight: 600; line-height: 1.2; }
  .about-text p { margin-top: 22px; font-size: 16px; line-height: 1.7; color: var(--ink-soft); }
  .about-photo {
    position: absolute; left: 600px; top: 0; width: 560px; height: 560px;
    background: linear-gradient(135deg, var(--photo-mid) 0%, var(--photo-light) 60%, #ededeb 100%);
  }
</style>
</head>
<body>
<div class="page">
  <header class="site-header">
    <div class="brand"><span class="brand-dot"></span>Westwind Air Co</div>
    <nav class="main-nav">
      <a href="#">Home</a>
      <a href="#">About Us</a>
      <a href="#">Services</a>
      <a href="#">Cleaning</a>
      <a href="#">Regasing</a>
      <a href="#">Commisioning</a>
      <a href="#">Air Balancing</a>
    </nav>
    <a class="btn" href="#">Book a Service
      <svg viewBox="0 0 14 14" fill="none" stroke="currentColor" stroke-width="1.6"><path d="M3 11 11 3M4.5 3H11v6.5"/></svg>
    </a>
  </header>

  <section class="hero">
    <div class="eyebrow">Quality Services</div>
    <h1>Quality Air Conditioning<br>Repairs, Service, and Installations</h1>
    <p>Our service is second to none; we have a team of experienced technicians that consistently deliver the best quality air conditioner repairs Perth has to offer. There are many different brands of air conditioning on the market, each with their own way of controlling the temperature of your home.</p>
    <a class="btn" href="#">Book a Service
      <svg viewBox="0 0 14 14" fill="none" stroke="currentColor" stroke-width="1.6"><path d="M3 11 11 3M4.5 3H11v6.5"/></svg>
    </a>
  </section>

  <section class="about">
    <div class="about-photo" role="img" aria-label="Photo of a friendly technician wearing a headset in a bright office"></div>
    <div class="about-text">
      <div class="eyebrow">About</div>
      <h2>Need a Technician?</h2>
      <p>Our call out fee includes the first half hour on site. In most cases our technician can find the fault and have your system running again well within that time.</p>
    </div>
  </section>
</div>
</body>
</html>
```